RM Cargoline businesscard project

RM Cargoline Ltd is a freshly founded small (3 employees), young (average age is 30 years) company, living from the road transportation market without own tools.
We would like to have an impressive, new-line, cool busines card for a freshly founded forwarding company on an overcrowded market which raises attention and makes the potential partners eager to work with us.

Target Market(s)

The main profile of the company is logistic/forwarding on road.

Industry/Entity Type

Freight Forwarding

Contact Information for Business Card

Name: Berki Zsófia
Title: general manager
mobile nr: +36-70/482-5193
fax nr: +36-1/534-9061
e-mail: zsofia.berki@rmcargoline.example
info@rmcargoline.example
website address: http://www.rmcargoline.example
and if possible maybe some funny or helpful info on the back

Requirements
Must have
• contact details above
Nice to have
• some really nice and catching back-side (info, graphics, useful tool info... anything)
Should not have
• trucks, road, ship, airplane on it...

```html
<!DOCTYPE html>
<html lang="en">
<head>
<meta charset="utf-8">
<title>RM Cargoline – Business Card</title>
<link href="https://fonts.googleapis.com/css2?family=Jost:wght@400;500&display=swap" rel="stylesheet">
<style>
  :root {
    --backdrop: #4a4a4a;
    --paper: #f7f7f7;
    --brand-blue: #5280b8;
    --ink: #2b2b2b;
    --ink-soft: #5a5a5a;
  }
  * { margin: 0; padding: 0; box-sizing: border-box; }
  html, body {
    width: 1200px; height: 750px; overflow: hidden;
    background: var(--backdrop);
    font-family: "Jost", sans-serif;
  }
  .card {
    position: absolute;
    top: 228px;
    width: 461px; height: 262px;
    background: var(--paper);
    overflow: hidden;
  }
  .card--front { left: 124px; }
  .card--back { left: 618px; }

  .brand-band {
    position: absolute; right: 0; top: 0;
    width: 205px; height: 100%;
    background: var(--brand-blue);
  }
  .company-name {
    position: absolute; left: 28px; top: 22px;
    font-weight: 500; font-size: 32px; line-height: 1;
    color: var(--ink); letter-spacing: -0.5px;
  }
  .person-name {
    position: absolute; left: 29px; top: 94px;
    font-weight: 400; font-size: 21px; line-height: 1;
    color: var(--brand-blue); letter-spacing: 0.3px;
  }
  .person-title {
    position: absolute; left: 30px; top: 120px;
    font-size: 14px; line-height: 1; color: var(--ink);
  }
  .contact-list {
    position: absolute; left: 30px; top: 150px;
    list-style: none;
  }
  .contact-list li {
    display: flex; align-items: center; gap: 6px;
    height: 18.5px;
    font-size: 11.5px; color: var(--ink-soft);
  }
  .contact-list svg { width: 11px; height: 11px; flex: none; fill: var(--brand-blue); }

  .back-lockup {
    position: absolute; left: 0; right: 0; top: 58px;
    display: flex; flex-direction: column; align-items: center; gap: 22px;
  }
  .back-lockup .mark-square {
    width: 62px; height: 62px; background: var(--brand-blue);
  }
  .back-lockup .company-name--back {
    font-weight: 500; font-size: 34px; line-height: 1;
    color: var(--ink); letter-spacing: -0.5px;
  }
</style>
</head>
<body>

<section class="card card--front">
  <div class="brand-band"></div>
  <div class="company-name">RM Cargoline</div>
  <div class="person-name">Berki Zsófia</div>
  <div class="person-title">General Manager</div>
  <ul class="contact-list">
    <li>
      <svg viewBox="0 0 12 12"><path d="M3 0h6v12H3zM4 1.5v8h4v-8z"/></svg>
      +36-70/482-5193
    </li>
    <li>
      <svg viewBox="0 0 12 12"><path d="M3 1h6v3H3zM0 5h12v5H10v2H2v-2H0zM3 8v3h6V8z"/></svg>
      +36-1/534-9061
    </li>
    <li>
      <svg viewBox="0 0 12 12"><path d="M0 2h12v8H0zM1 3l5 4 5-4z" fill-rule="evenodd"/></svg>
      zsofia.berki@rmcargoline.example
    </li>
    <li>
      <svg viewBox="0 0 12 12"><path d="M0 2h12v8H0zM1 3l5 4 5-4z" fill-rule="evenodd"/></svg>
      info@rmcargoline.example
    </li>
    <li>
      <svg viewBox="0 0 12 12"><circle cx="6" cy="6" r="6"/><path d="M3 4h3v3H4zM7 7h2v2H7z" fill="#f7f7f7"/></svg>
      www.rmcargoline.example
    </li>
  </ul>
</section>

<section class="card card--back">
  <div class="back-lockup">
    <div class="mark-square"></div>
    <div class="company-name--back">RM Cargoline</div>
  </div>
</section>

</body>
</html>
```